Hollowbrook Yard Services - Needs a business card! Easy JOB!

I need a business card for a new company called Hollowbrook Yard Services. I will be offering the below services.

I am relatively open for ideas, so please be at your creative best.

I think I will list all the services offered on the rear of the card.

- Gardening
- Lawn Care
- Hedge Trimming
- Rubbish Removal
- Weeding/Spraying
- Landscaping
- Gutter Cleaning
- Solar Panel Cleaning
- Irrigation
- Pruning
- On-Site Mulching
- Ask for other services

I am still a little undecided on the colours. I prefer the logos with the Blue text, but I am open for ideas ( the logo/texts colours are not final).

Please use the catch phrase "What can Hollowbrook do for you?"

Here are the required details.

Hollowbrook Yard Services

Miles Fenwarick (owner)
Ph: 1300 555 014
Mob: 0400 555 286

miles@hollowbrookyard.com.au
www.hollowbrookyard.com.au
facebook.com/HollowbrookYard
twitter.com/HollowbrookYard
ABN: 555 019 472 ( this can be in smaller text somewhere, this is the least important )

Thankyou in advance! And good luck.

regards,
Miles
Updates

Hi everyone, please make sure you include the phrase "What can Hollowbrook do for you?" on the designs.

thanks,
Miles

Definitely liking the focus on a majority of the design on the blue colour from the logo. Also a splash of green in the plant.

Please make sure you list the services provided on the rear of the card. thanks.

With the service listing, please make "ask for other services" stand out, either a different colour or position or size... as long as it is more noticeable than the other services listed. Thanks.

Industry/Entity Type

Business

Requirements
Must have
• - use the font supplied (Brandon Family Font)
- use of the catch phrase "What can Hollowbrook do for you?"
- Double sided design
- Chatterly and Quipster logos/links
- Please use symbol/picture for "phone" "mobile" "email" instead of using the words.
- List the services provided on the rear of the card

```html
<!DOCTYPE html>
<html lang="en">
<head>
<meta charset="utf-8">
<title>Hollowbrook Yard Services – Business Card</title>
<link rel="stylesheet" href="https://fonts.googleapis.com/css2?family=Outfit:wght@300;400;500;600;700&display=swap">
<style>
  :root {
    --brand-blue: #1d4f9c;
    --brand-green: #7ab648;
    --text-grey: #5a5f66;
    --muted-grey: #b9bec4;
    --divider: #d3d6da;
    --card-white: #ffffff;
    --page-bg: #eceeed;
    --social-light: #4aa8d8;
  }
  * { box-sizing: border-box; margin: 0; padding: 0; }
  html, body {
    width: 1200px; height: 1038px; overflow: hidden;
    background: var(--page-bg);
    font-family: "Outfit", sans-serif;
  }
  .canvas { position: relative; width: 1200px; height: 1038px; }
  .card {
    position: absolute; left: 210px; width: 780px; height: 477px;
    background: var(--card-white);
    box-shadow: 0 6px 22px rgba(0,0,0,0.12);
    overflow: hidden;
  }
  .card--front { top: 27px; }
  .card--back { top: 534px; }

  /* Front: brand side */
  .brand {
    position: absolute; left: 0; top: 0; width: 410px; height: 100%;
    display: flex; flex-direction: column; align-items: center;
  }
  .brand__mark {
    margin-top: 110px; width: 96px; height: 96px; border-radius: 50%;
    background: var(--brand-green);
  }
  .brand__name {
    margin-top: 26px; color: var(--brand-blue);
    font-weight: 700; font-size: 34px; line-height: 1.05;
    text-align: center; text-transform: uppercase; letter-spacing: 0.5px;
  }
  .brand__tagline {
    position: absolute; bottom: 60px; left: 0; width: 100%;
    text-align: center; color: var(--brand-green);
    font-size: 24px; font-weight: 400;
  }
  .divider {
    position: absolute; left: 410px; top: 22px; bottom: 22px;
    width: 2px; background: var(--divider);
  }

  /* Front: contact side */
  .contact { position: absolute; left: 448px; top: 40px; width: 310px; }
  .contact__name { color: var(--brand-blue); font-size: 31px; font-weight: 600; }
  .contact__role { color: var(--text-grey); font-size: 14px; margin-top: 2px; }
  .contact__list { list-style: none; margin-top: 22px; }
  .contact__item {
    display: flex; align-items: center; gap: 12px;
    color: var(--text-grey); height: 32px;
  }
  .contact__item--phone { font-size: 22px; font-weight: 500; }
  .contact__item--email { font-size: 16px; }
  .contact__item svg { width: 20px; height: 20px; fill: var(--text-grey); flex: none; }
  .contact__web {
    margin-top: 26px; color: var(--brand-green); font-size: 17px; font-weight: 500;
  }
  .social { list-style: none; margin-top: 14px; }
  .social__item {
    display: flex; align-items: center; gap: 12px;
    color: var(--text-grey); font-size: 16px; height: 30px;
  }
  .social__dot { width: 16px; height: 16px; border-radius: 50%; flex: none; }
  .social__dot--chatterly { background: var(--brand-blue); }
  .social__dot--quipster { background: var(--social-light); }
  .contact__abn { margin-top: 20px; color: var(--muted-grey); font-size: 14px; }

  /* Back: services */
  .services {
    position: absolute; left: 56px; right: 56px; top: 38px;
    display: flex; justify-content: space-between;
  }
  .services__column { list-style: none; }
  .services__column--right { text-align: right; }
  .services__item {
    color: var(--brand-green); font-size: 27px; font-weight: 500; line-height: 44px;
  }
  .services__item--highlight { color: var(--brand-blue); font-weight: 600; }
  .back__tagline {
    position: absolute; left: 0; right: 0; bottom: 42px;
    text-align: center; color: var(--brand-blue);
    font-size: 40px; font-style: italic; font-weight: 500;
  }
</style>
</head>
<body>
<main class="canvas">

  <section class="card card--front" aria-label="Business card front">
    <div class="brand">
      <div class="brand__mark" aria-hidden="true"></div>
      <h1 class="brand__name">Hollowbrook<br>Yard Services</h1>
      <p class="brand__tagline">What can Hollowbrook do for you?</p>
    </div>

    <div class="divider" aria-hidden="true"></div>

    <div class="contact">
      <h2 class="contact__name">Miles Fenwarick</h2>
      <p class="contact__role">Owner</p>
      <ul class="contact__list">
        <li class="contact__item contact__item--phone">
          <svg viewBox="0 0 24 24" aria-label="Phone"><path d="M6.6 10.8a15.1 15.1 0 0 0 6.6 6.6l2.2-2.2a1 1 0 0 1 1-.25 11.4 11.4 0 0 0 3.6.57 1 1 0 0 1 1 1V20a1 1 0 0 1-1 1A17 17 0 0 1 3 4a1 1 0 0 1 1-1h3.5a1 1 0 0 1 1 1c0 1.25.2 2.45.57 3.57a1 1 0 0 1-.25 1z"/></svg>
          1300 555 014
        </li>
        <li class="contact__item contact__item--phone">
          <svg viewBox="0 0 24 24" aria-label="Mobile"><path d="M7 1h10a2 2 0 0 1 2 2v18a2 2 0 0 1-2 2H7a2 2 0 0 1-2-2V3a2 2 0 0 1 2-2zm0 3v14h10V4zm5 15.2a1.2 1.2 0 1 0 0 2.4 1.2 1.2 0 0 0 0-2.4z"/></svg>
          0400 555 286
        </li>
        <li class="contact__item contact__item--email">
          <svg viewBox="0 0 24 24" aria-label="Email"><path d="M3 5h18a1 1 0 0 1 1 1v12a1 1 0 0 1-1 1H3a1 1 0 0 1-1-1V6a1 1 0 0 1 1-1zm1 2.3V17h16V7.3l-8 5.2zM5.2 7 12 11.4 18.8 7z"/></svg>
          miles@hollowbrookyard.com.au
        </li>
      </ul>
      <p class="contact__web">www.hollowbrookyard.com.au</p>
      <ul class="social">
        <li class="social__item"><span class="social__dot social__dot--chatterly" aria-label="Chatterly"></span>chatterly.com/HollowbrookYard</li>
        <li class="social__item"><span class="social__dot social__dot--quipster" aria-label="Quipster"></span>quipster.com/HollowbrookYard</li>
      </ul>
      <p class="contact__abn">ABN: 555 019 472</p>
    </div>
  </section>

  <section class="card card--back" aria-label="Business card back">
    <div class="services">
      <ul class="services__column">
        <li class="services__item">Gardening</li>
        <li class="services__item">Lawn Care</li>
        <li class="services__item">Hedge Trimming</li>
        <li class="services__item">Rubbish Removal</li>
        <li class="services__item">Weeding/Spraying</li>
        <li class="services__item">Landscaping</li>
      </ul>
      <ul class="services__column services__column--right">
        <li class="services__item">Gutter Cleaning</li>
        <li class="services__item">Solar Panel Cleaning</li>
        <li class="services__item">Irrigation</li>
        <li class="services__item">Pruning</li>
        <li class="services__item">On-Site Mulching</li>
        <li class="services__item services__item--highlight">Ask for other services</li>
      </ul>
    </div>
    <p class="back__tagline">What can Hollowbrook do for you?</p>
  </section>

</main>
</body>
</html>
```